Business Card Design for BT Wine:

I'm looking for a card that has the following.
Front:
- Merlot Colored
- stripe down the middle in silver or gold flake
- BT in block like thick letters with gold or silver flake above stripe
-Wine: below stripe
- a grape bunch that is at the end of the stripe that is made so it can be printed as embossed
Back:
- line down the middle of card in Merlot, card is white background
- to the left Marla Boyce, (next line) Owner, (next line) Certified Sommelier, GRV
- to the right (listed) restaurant consulting, wine tours, personal tastings, event planning, personal wine buying
- add embossed grape bunch
Also, looking for a piece that slides over like a envelope for a room key for a hotel that says "We met @ DUNVAL" and possibly a file for that, that I can edit.
Would like card to be printed on a thicker cardstock

```html
<!DOCTYPE html>
<html lang="en">
<head>
<meta charset="utf-8">
<title>BT Wine — Business Card</title>
<link href="https://fonts.googleapis.com/css2?family=Arimo:wght@400;700&family=Oswald:wght@700&display=swap" rel="stylesheet">
<style>
  :root {
    --merlot: #4a0a14;
    --gold: #c08400;
    --silver-light: #ececec;
    --silver-mid: #c4c4c4;
    --silver-dark: #7a7a7c;
    --paper: #ffffff;
    --ink: #1a1a1a;
    --backdrop: #e9e9ea;
    --grape-tone: #b9b3b5;
  }
  * { margin: 0; padding: 0; box-sizing: border-box; }
  html, body {
    width: 1200px; height: 1000px; overflow: hidden;
    background: var(--backdrop);
    font-family: "Arimo", Arial, sans-serif;
  }
  .canvas { position: relative; width: 1200px; height: 1000px; }
  .card {
    position: absolute; left: 224px; width: 752px; height: 430px;
    overflow: hidden; box-shadow: 0 6px 18px rgba(0,0,0,0.18);
  }
  /* Front */
  .card-front { top: 50px; background: var(--merlot); }
  .front-monogram {
    position: absolute; left: 272px; top: 62px;
    font-weight: 700; font-size: 138px; line-height: 1; letter-spacing: -2px;
    color: var(--gold);
  }
  .front-stripe {
    position: absolute; left: 0; top: 212px; width: 100%; height: 52px;
    background: linear-gradient(90deg, var(--silver-mid) 0%, var(--silver-light) 30%, var(--silver-mid) 65%, var(--silver-dark) 100%);
  }
  .front-label {
    position: absolute; left: 51px; top: 289px;
    font-size: 40px; color: var(--paper); letter-spacing: 0.5px;
  }
  .grape-emboss {
    position: absolute; border-radius: 40% 40% 50% 50%;
    background: radial-gradient(circle at 45% 40%, #d8d3d5 0%, var(--grape-tone) 100%);
    opacity: 0.55;
  }
  .card-front .grape-emboss { left: 628px; top: 96px; width: 118px; height: 162px; }
  /* Back */
  .card-back { top: 520px; background: var(--paper); }
  .back-divider {
    position: absolute; left: 375px; top: 0; width: 2px; height: 100%;
    background: var(--merlot);
  }
  .back-identity {
    position: absolute; right: 400px; top: 40px; text-align: left; width: 330px;
  }
  .back-name {
    font-family: "Oswald", "Arial Narrow", sans-serif; font-weight: 700;
    font-size: 36px; color: var(--ink); text-transform: uppercase; letter-spacing: 1px;
  }
  .back-role { font-size: 30px; color: #444; margin-top: 4px; }
  .back-cert { font-size: 24px; color: #555; margin-top: 12px; text-align: right; line-height: 1.3; }
  .back-services {
    position: absolute; left: 405px; top: 44px; list-style: none;
    font-size: 24px; line-height: 1.25; color: var(--ink);
  }
  .card-back .grape-emboss { left: 500px; top: 300px; width: 82px; height: 110px; }
</style>
</head>
<body>
<main class="canvas">
  <section class="card card-front" aria-label="BT Wine business card, front">
    <div class="front-monogram">BT</div>
    <div class="front-stripe"></div>
    <div class="front-label">WINE</div>
    <div class="grape-emboss" role="img" aria-label="Embossed grape bunch outline with leaf"></div>
  </section>

  <section class="card card-back" aria-label="BT Wine business card, back">
    <div class="back-divider"></div>
    <div class="back-identity">
      <div class="back-name">Marla Boyce</div>
      <div class="back-role">Owner</div>
      <div class="back-cert">Certified Sommelier,<br>GRV</div>
    </div>
    <ul class="back-services">
      <li>Restaurant Consulting,</li>
      <li>Wine Tours,</li>
      <li>Personal Tastings,</li>
      <li>Event Planning,</li>
      <li>Personal Wine</li>
      <li>Buying</li>
    </ul>
    <div class="grape-emboss" role="img" aria-label="Embossed grape bunch outline"></div>
  </section>
</main>
</body>
</html>
```